Brindle's Online: Logo Banner Graphic-

We are building our website and need to take our current logo ( that you designed) and create a banner with our tagline. The key focus is that we need to play with color on the logo that fits to the current background- The goal is to make it "pop" without making it look cheap. This is a high end lifestyle brand.

We are open to color( and will consider changing the background for the right look and open to you creating a new background to work with the design) but keeping in mind it needs to have color that represent luxury, money, leisure.

The sizing/pixels should be
2510 x 1671 px
8.37 x 5.57p

Currently you can look at the prototype website at

www.brindlesonline-example.com

Please let me know if you have any questions.

Please find a JPEG and PDF of my actual logo updated in the files section of this contest Added Friday, January 6, 2017

Target Market(s)

30 plus

Industry/Entity Type

Building

Font styles to use
Sans Serif

Requirements
Must have
• Logo and tagline in header
Nice to have
• open
Should not have
• color to make it pop on website. It needs to be professional and polished not cheap looking.

```html
<!DOCTYPE html>
<html lang="en">
<head>
<meta charset="utf-8">
<title>Brindle's Online – Header Banner</title>
<link rel="stylesheet" href="https://fonts.googleapis.com/css2?family=Libre+Baskerville:ital@0;1&family=Kaushan+Script&family=PT+Sans:wght@400;700&family=Open+Sans:wght@400;700&display=swap">
<style>
  :root {
    --canvas: #000000;
    --wood-light: #a8672e;
    --wood-mid: #7a4519;
    --wood-dark: #3a1d0a;
    --wood-deep: #241106;
    --ink-brown: #3b1e0b;
    --nav-band: #0b0604;
    --nav-text: #ffffff;
    --rule: #e8e0d8;
    --panel: #f5f5f2;
    --card: #ffffff;
    --card-border: #e2e2e2;
    --title-grey: #555555;
    --price-green: #5cb85c;
    --arrow-grey: #8a8a8a;
  }
  * { margin: 0; padding: 0; box-sizing: border-box; }
  html, body { width: 1200px; height: 1000px; overflow: hidden; background: var(--canvas); }
  .page { position: relative; width: 1200px; height: 1000px; }

  .wood-header {
    position: absolute; left: 0; top: 120px; width: 1200px; height: 296px;
    background:
      radial-gradient(ellipse 65% 70% at 50% 50%, var(--wood-light) 0%, var(--wood-mid) 60%, var(--wood-dark) 100%);
  }
  .wood-lower {
    position: absolute; left: 0; top: 416px; width: 1200px; height: 470px;
    background: radial-gradient(ellipse 70% 80% at 50% 40%, #6b3a16 0%, #4a250d 55%, var(--wood-deep) 100%);
  }

  .brand-mark {
    position: absolute; left: 110px; top: 186px; width: 182px; height: 182px;
    border: 6px solid var(--ink-brown); border-radius: 50%;
    display: flex; align-items: center; justify-content: center; text-align: center;
  }
  .brand-name {
    font-family: "Libre Baskerville", serif; font-size: 24px; line-height: 1.15;
    color: var(--ink-brown);
  }

  .tagline { position: absolute; left: 0; top: 0; color: var(--ink-brown); }
  .tagline-lead {
    position: absolute; left: 328px; top: 186px;
    font-family: "Libre Baskerville", serif; font-size: 38px; white-space: nowrap;
  }
  .tagline-main {
    position: absolute; left: 322px; top: 212px;
    font-family: "Kaushan Script", cursive; font-size: 70px; white-space: nowrap; letter-spacing: -1px;
  }
  .tagline-tail {
    position: absolute; left: 506px; top: 294px;
    font-family: "Libre Baskerville", serif; font-size: 36px; white-space: nowrap;
  }
  .tagline-tail em { font-family: "Kaushan Script", cursive; font-style: normal; font-size: 34px; }

  .main-nav {
    position: absolute; left: 0; top: 414px; width: 1200px; height: 60px;
    background: var(--nav-band);
  }
  .main-nav::before, .main-nav::after {
    content: ""; position: absolute; left: 25px; width: 1142px; height: 2px; background: var(--rule);
  }
  .main-nav::before { top: 1px; }
  .main-nav::after { bottom: 1px; }
  .main-nav ul {
    list-style: none; display: flex; justify-content: center; gap: 36px;
    padding-top: 20px; padding-left: 28px;
  }
  .main-nav li {
    font-family: "PT Sans", sans-serif; font-weight: 700; font-size: 17px;
    letter-spacing: 1.4px; color: var(--nav-text);
  }

  .product-panel {
    position: absolute; left: 89px; top: 495px; width: 1038px; height: 289px;
    background: var(--panel);
  }
  .panel-title {
    position: absolute; left: 55px; top: 19px;
    font-family: "Open Sans", sans-serif; font-size: 15px; color: var(--title-grey);
  }
  .search-box {
    position: absolute; left: 770px; top: 10px; width: 220px; height: 33px;
    background: var(--card); border: 1px solid var(--card-border);
  }
  .search-box svg { position: absolute; left: 10px; top: 7px; }

  .product-card {
    position: absolute; top: 52px; width: 221px; height: 221px;
    background: var(--card); border: 1px solid var(--card-border);
  }
  .product-photo { width: 100%; height: 176px; }
  .product-name {
    font-family: "Open Sans", sans-serif; font-weight: 700; font-size: 10.5px; color: #333;
    padding: 6px 0 0 4px; white-space: nowrap;
  }
  .product-price {
    font-family: "Open Sans", sans-serif; font-size: 11px; color: var(--price-green);
    padding: 2px 0 0 4px;
  }

  .carousel-arrow {
    position: absolute; top: 612px; width: 39px; height: 38px; background: var(--arrow-grey);
    display: flex; align-items: center; justify-content: center;
  }
</style>
</head>
<body>
<div class="page">
  <div class="wood-header" role="img" aria-label="Warm wooden plank texture with dark vignette"></div>
  <div class="wood-lower" role="img" aria-label="Dark stained wooden plank background"></div>

  <div class="brand-mark"><span class="brand-name">Brindle's<br>Online</span></div>

  <div class="tagline">
    <span class="tagline-lead">Delivering</span>
    <span class="tagline-main">Simplified Reliable Smoking</span>
    <span class="tagline-tail">products <em>to fit your</em> lifestyle</span>
  </div>

  <nav class="main-nav">
    <ul>
      <li>HOME</li><li>ABOUT US</li><li>VAPES</li><li>ACCESSORIES</li><li>BLOG</li><li>CONTACT US</li>
    </ul>
  </nav>

  <section class="product-panel">
    <h2 class="panel-title">Vaporizers</h2>
    <div class="search-box">
      <svg width="18" height="18" viewBox="0 0 18 18"><circle cx="7" cy="7" r="5" fill="none" stroke="#999" stroke-width="2"/><line x1="11" y1="11" x2="16" y2="16" stroke="#999" stroke-width="2"/></svg>
    </div>

    <article class="product-card" style="left:54px">
      <div class="product-photo" role="img" aria-label="Product photo of two handheld vaporizers on grey" style="background:linear-gradient(90deg,#4a4a4a,#5c5c5c 45%,#8a3d18 75%,#555)"></div>
      <p class="product-name">Lorem ipsum dolor sit amet, consecte-</p>
      <p class="product-price">USD 40.00</p>
    </article>
    <article class="product-card" style="left:292px">
      <div class="product-photo" role="img" aria-label="Product photo of a boxed vaporizer kit in blue and white" style="background:linear-gradient(180deg,#f2f2f2 0%,#dfe6f2 50%,#1f5fd0 100%)"></div>
      <p class="product-name">Lorem ipsum dolor sit amet, consecte-</p>
      <p class="product-price">USD 35.00</p>
    </article>
    <article class="product-card" style="left:531px">
      <div class="product-photo" role="img" aria-label="Product photo of a small engraved wooden vaporizer" style="background:radial-gradient(ellipse 45% 35% at 50% 45%,#c48a5e,#d9a882 70%,#ffffff 72%)"></div>
      <p class="product-name">Lorem ipsum dolor sit amet, consecte-</p>
      <p class="product-price">USD 23.00</p>
    </article>
    <article class="product-card" style="left:770px">
      <div class="product-photo" role="img" aria-label="Product photo of a silver vaporizer with accessories on white" style="background:radial-gradient(ellipse 50% 30% at 50% 55%,#cfcfcf,#f4f4f4 80%);border-bottom:3px solid #333"></div>
      <p class="product-name">Lorem ipsum dolor sit amet, consecte-</p>
      <p class="product-price">USD 28.00</p>
    </article>
  </section>

  <div class="carousel-arrow" style="left:80px">
    <svg width="16" height="16" viewBox="0 0 16 16"><path d="M8 2 L2 8 L8 14 M14 2 L8 8 L14 14" fill="none" stroke="#fff" stroke-width="1.6"/></svg>
  </div>
  <div class="carousel-arrow" style="left:1097px">
    <svg width="16" height="16" viewBox="0 0 16 16"><path d="M2 2 L8 8 L2 14 M8 2 L14 8 L8 14" fill="none" stroke="#fff" stroke-width="1.6"/></svg>
  </div>
</div>
</body>
</html>
```